UK Based Internet hosting Company wants a vibrant eCommerce site designed.

We have only just had our logo and brand designed by Pixel Harbor which went so well that we would like to open up our website design project on here too.

The company is called 'Our Server Lantern' and we provide a range of website hosting, dedicated server, domain name and email solutions that people will be able to purchase online in neatly packaged options from the outset.

Our logo and brand is bright turquoise, black & white (samples of branding will be attached with this project) but we would like the website to be very vibrant with good use of white space rather than a black website.

We want to appeal to end users so web designers, developers and people who would like to host their website. But we also want to appeal to resellers that would like to resell our hosting packages too.

We want a big push on social media and blogging on the site as we would like our brand to be 100% up with Chatterly, Quipster, workRing, Vidoplex and Orbitly+. It would be great to have this integrated into the site with share buttons and rating buttons etc.

We would like to see a homepage initially with a view to providing several page layers down to help our in-house developers hook in our back-end into this front end effectively.

Great customer experience and an easy to navigate journey to the checkout when purchasing the hosting packages is paramount !!

We like how the following sites are set-out and presented:

www.plumwebnode.uk
http://www.tagvault.co.uk
https://www.zq7.net/web-hosting/

Target Market(s)

We have 3 target markets.

Target market 1 - end users, consumers such as Web Designers, Developers and small businesses.

Target Market 2 - Resellers, small businesses that would like to resell our services.

Target Market 3 - Medium to large businesses that would like more of a bespoke solution.

Industry/Entity Type

Internet

Requirements
Must have
• Colourful, bright, bold, easy to navigate and to purchase packages.
• Plenty of call to actions, social media, ratings.
• Video case studies and testimonials would be nice.

```html
<!DOCTYPE html>
<html lang="en">
<head>
<meta charset="utf-8">
<title>Our Server Lantern – Web Hosting</title>
<link rel="stylesheet" href="https://fonts.googleapis.com/css2?family=Lato:wght@300;400;700;900&family=Roboto+Condensed:wght@400;700&display=swap">
<style>
:root{
  --teal:#1fbab5;
  --teal-dark:#16a39f;
  --teal-light:#3fcfc6;
  --ink:#2a2f33;
  --text:#555b60;
  --muted:#8a9095;
  --line:#d6d9db;
  --panel:#f5f6f6;
  --navy:#1c2530;
  --gold:#f3b51c;
  --white:#ffffff;
}
*{box-sizing:border-box;margin:0;padding:0}
html,body{width:1200px;height:2875px;overflow:hidden}
body{font-family:"Lato",Arial,sans-serif;color:var(--text);background:var(--white);position:relative}
ul{list-style:none}

/* header */
.site-header{position:absolute;left:0;top:0;width:1200px;height:100px;background:var(--white)}
.brand{position:absolute;left:52px;top:14px;display:flex;align-items:center;gap:12px}
.brand-dot{width:50px;height:50px;border-radius:50%;background:var(--teal)}
.brand-name{font-weight:700;font-size:22px;line-height:24px;color:var(--ink)}
.call-us{position:absolute;left:370px;top:13px;font-size:15px;font-weight:700;color:var(--ink);letter-spacing:.3px}
.call-us span{color:var(--teal);font-style:italic;font-weight:400}
.basket{position:absolute;left:782px;top:10px;font-size:14px;color:var(--ink);display:flex;align-items:center;gap:6px}
.util-nav{position:absolute;left:878px;top:0;width:268px;height:38px;background:#eceded;display:flex;justify-content:space-around;align-items:center;font-size:12.5px;color:var(--ink);letter-spacing:.4px}
.main-nav{position:absolute;left:316px;top:54px;width:884px;height:46px;background:linear-gradient(90deg,var(--teal-light),var(--teal));clip-path:polygon(22px 0,100% 0,100% 100%,0 100%)}
.main-nav ul{display:flex;align-items:center;height:46px;padding-left:40px}
.main-nav li{font-size:12.5px;font-weight:700;color:var(--white);letter-spacing:.4px;padding:6px 17px}
.main-nav li.active{background:var(--white);color:var(--ink)}

/* hero */
.hero{position:absolute;left:0;top:100px;width:1200px;height:414px;background:linear-gradient(100deg,#6c8f8a 0%,#9aa7a3 25%,#c8c3bb 50%,#ddd6cc 75%,#b9b3ab 100%)}
.hero-text{position:absolute;left:618px;top:124px;width:440px;text-align:center}
.hero-text .kicker{font-size:27px;color:var(--white);font-weight:700;text-shadow:0 1px 3px rgba(0,0,0,.3)}
.hero-text .title{font-size:29px;color:var(--teal);font-weight:900;margin-top:10px;white-space:nowrap}
.hero-buttons{display:flex;justify-content:center;gap:10px;margin-top:16px}
.btn{font-size:13px;font-weight:700;padding:8px 14px;letter-spacing:.3px}
.btn-teal{background:var(--teal);color:var(--white)}
.btn-light{background:var(--white);color:var(--ink)}
.hero-arrow{position:absolute;top:178px;width:42px;height:42px;border-radius:50%;background:rgba(40,45,50,.55);display:flex;align-items:center;justify-content:center}

/* domain search */
.domain-search{position:absolute;left:0;top:514px;width:1200px;height:96px;background:linear-gradient(90deg,#4cc7b9,var(--teal) 60%,#16aaa6)}
.domain-search label{position:absolute;left:52px;top:36px;color:var(--white);font-weight:700;font-size:20px}
.domain-input{position:absolute;left:272px;top:27px;width:619px;height:44px;background:var(--white);font-size:15px;color:var(--muted);padding:12px 16px}
.domain-btn{position:absolute;left:914px;top:27px;width:232px;height:44px;background:linear-gradient(#f4f4f4,#d9dbdb);font-family:"Roboto Condensed",Arial,sans-serif;font-size:24px;color:var(--ink);text-align:center;line-height:44px}

/* section intro */
.section-intro{position:absolute;left:52px;width:1094px}
.section-intro .label{font-size:24px;font-weight:300;letter-spacing:1.5px;color:var(--ink);text-transform:uppercase}
.section-intro .big{font-size:38px;font-weight:900;color:var(--teal);letter-spacing:1px;text-transform:uppercase;line-height:44px}
.section-intro .rule{position:absolute;left:230px;top:0;width:2px;height:84px;background:var(--line)}
.section-intro p{position:absolute;left:254px;top:-2px;width:840px;font-size:12.6px;line-height:19px}
.divider{position:absolute;left:52px;width:1094px;height:2px;background:var(--line)}
.divider::before{content:"";position:absolute;left:0;top:0;width:44px;height:2px;background:var(--ink)}
.divider::after{content:"";position:absolute;left:44px;top:0;width:50px;height:2px;background:var(--teal)}

/* pricing */
.plan{position:absolute;top:797px;width:232px;height:209px;background:var(--white);box-shadow:0 2px 8px rgba(0,0,0,.15);text-align:center;padding-top:48px;color:var(--ink)}
.plan.featured{background:var(--teal);color:var(--white)}
.plan .from{font-size:11px;letter-spacing:.5px}
.plan .price{font-size:23px;font-weight:900;margin-top:8px}
.plan .name{font-size:15px;margin-top:6px;letter-spacing:.3px}
.plan .note{font-size:11px;line-height:14px;margin:10px 30px 0}
.plan-ribbon{position:absolute;top:1006px;width:232px;height:20px}

/* features */
.features{position:absolute;left:0;top:1058px;width:1200px;height:571px;background:var(--panel)}
.feature{position:absolute;width:500px}
.feature svg{position:absolute;left:0;top:0}
.feature h3{position:absolute;left:103px;top:0;font-size:13px;font-weight:700;color:var(--ink)}
.feature p{position:absolute;left:103px;top:26px;width:396px;font-size:12.3px;line-height:19px}

/* blog */
.blog{position:absolute;left:0;top:1629px;width:1200px;height:451px;background:linear-gradient(90deg,#2a2d31,#3b3f43 50%,#2a2d31)}
.blog .section-intro .label{color:var(--white)}
.blog .section-intro p{color:#d7dadc}
.blog .divider{background:#55595d}
.post{position:absolute;top:1831px;width:540px}
.post-date{position:absolute;left:0;top:0;width:53px;height:51px;background:var(--teal);color:var(--white);text-align:center;font-weight:700;font-size:15px;line-height:20px;padding-top:5px}
.post-date sup{font-size:9px}
.post h3{position:absolute;left:67px;top:3px;font-size:17px;font-weight:400;color:var(--white);white-space:nowrap}
.post .byline{position:absolute;left:67px;top:35px;font-size:12px;font-style:italic;color:#d7dadc;white-space:nowrap}
.post .byline .stars{color:var(--gold);font-style:normal;margin-left:10px;letter-spacing:3px}
.post-image{position:absolute;left:67px;top:71px;width:163px;height:88px;border:2px solid #e6e6e6}
.post p{position:absolute;left:255px;top:71px;width:270px;font-size:12.4px;line-height:17px;color:#e4e6e7}
.share{position:absolute;left:255px;top:176px;display:flex;gap:6px}
.share span{width:23px;height:23px;background:#cfd2d4}

/* testimonials */
.quote{position:absolute;font-size:12.4px;line-height:17px;color:var(--ink);font-weight:400}
.quote strong{display:block;font-size:12.6px;font-weight:700}
.quote .role{font-weight:700;display:block;margin-bottom:6px}
.quote .role em{color:var(--teal);font-style:normal;font-weight:400}
.avatar{position:absolute;border-radius:50%;border:5px solid var(--teal)}

/* footer */
.site-footer{position:absolute;left:0;top:2517px;width:1200px;height:307px;background:var(--navy)}
.follow-panel{position:absolute;left:767px;top:0;width:433px;height:307px;background:linear-gradient(135deg,var(--teal-light),var(--teal-dark));clip-path:polygon(115px 0,100% 0,100% 100%,0 100%)}
.foot-col{position:absolute;top:35px}
.foot-col h4{font-size:19px;font-weight:400;color:var(--white);letter-spacing:.5px;padding-bottom:10px;border-bottom:1px solid #3e4955;width:160px;white-space:nowrap}
.foot-col ul{margin-top:12px}
.foot-col li{font-size:12.6px;color:#e4e7ea;line-height:23.6px}
.foot-col li::before{content:"→";color:#c7cdd2;margin-right:10px}
.foot-sep{position:absolute;top:35px;width:1px;height:250px;background:#333e4a}
.contact-row{display:flex;gap:12px;margin-top:14px;font-size:12.4px;color:#e4e7ea;line-height:16px}
.contact-row .ico{flex:0 0 22px;height:22px;border-radius:50%;background:var(--teal);display:flex;align-items:center;justify-content:center}
.follow h4{font-size:19px;font-weight:400;color:var(--white);letter-spacing:.5px;padding-bottom:10px;border-bottom:1px solid rgba(255,255,255,.5);width:240px;white-space:nowrap}
.follow .socials{display:flex;gap:12px;margin:18px 0 22px}
.follow .socials span{width:24px;height:24px;border-radius:50%;background:rgba(255,255,255,.25);border:1px solid rgba(255,255,255,.7)}
.email-field{width:242px;height:28px;background:var(--white);border-radius:3px;font-size:12px;color:var(--ink);padding:7px 10px;margin-top:16px}
.submit{display:inline-block;margin-top:10px;background:var(--white);color:var(--ink);font-size:12px;font-weight:700;padding:6px 12px;border-radius:2px}
.bottom-bar{position:absolute;left:0;top:2824px;width:1200px;height:51px;background:#e9eaea;font-size:12px;color:var(--ink)}
.bottom-bar .copy{position:absolute;left:52px;top:18px}
.bottom-bar nav{position:absolute;right:52px;top:18px;display:flex}
.bottom-bar nav span{padding:0 13px;border-left:1px solid #b9bcbe}
.bottom-bar nav span:first-child{border-left:0}
</style>
</head>
<body>

<header class="site-header">
  <div class="brand"><span class="brand-dot"></span><span class="brand-name">Our Server<br>Lantern</span></div>
  <div class="call-us">CALL US NOW: <span>+1 800 555 0142</span></div>
  <div class="basket">Basket
    <svg width="26" height="18" viewBox="0 0 26 18"><path d="M1 2h4l3 10h13l3-8H7" fill="none" stroke="#2a2f33" stroke-width="2"/><circle cx="10" cy="16" r="1.8" fill="#2a2f33"/><circle cx="19" cy="16" r="1.8" fill="#2a2f33"/></svg>
  </div>
  <ul class="util-nav"><li>LOGIN</li><li>SUPPORT</li><li>BLOG</li></ul>
  <nav class="main-nav">
    <ul><li class="active">HOME</li><li>ABOUT</li><li>DOMAINS</li><li>EMAIL</li><li>HOSTING</li><li>DEDICATED SERVER</li><li>FAQ</li><li>CONTACT</li></ul>
  </nav>
</header>

<section class="hero" role="img" aria-label="Photo of a smiling woman in glasses working on a laptop in a bright living room">
  <div class="hero-arrow" style="left:25px"><svg width="14" height="18"><path d="M10 2 3 9l7 7" fill="none" stroke="#fff" stroke-width="2"/></svg></div>
  <div class="hero-arrow" style="left:1133px"><svg width="14" height="18"><path d="M4 2l7 7-7 7" fill="none" stroke="#fff" stroke-width="2"/></svg></div>
  <div class="hero-text">
    <div class="kicker">Empowering You To Take</div>
    <div class="title">Control Of Your Internet Lantern</div>
    <div class="hero-buttons"><span class="btn btn-teal">HOSTING PLAN</span><span class="btn btn-light">CONTACT US</span></div>
  </div>
</section>

<section class="domain-search">
  <label>Domain Name Search</label>
  <div class="domain-input">www.</div>
  <div class="domain-btn">Search Domains</div>
</section>

<!-- welcome -->
<div class="section-intro" style="top:642px">
  <div class="label" style="font-size:26px">Welcome to</div>
  <div class="brand" style="position:relative;left:0;top:14px;gap:10px"><span class="brand-dot" style="width:46px;height:46px"></span><span class="brand-name" style="font-size:20px;line-height:22px">Our Server<br>Lantern</span></div>
  <div class="rule"></div>
  <p>Aenean efficitur mauris faucibus ante viverra, vitae malesuada nisl convallis. Fusce rutrum, neque tempor euismod lacinia, eros lorem imperdiet felis, id sollicitudin orci ligula id mauris. Quisque imperdiet at massa nec sagittis. Vestibulum finibus interdum consectetur. Morbi tempus, elit a luctus sodales, mauris est rhoncus urna, quis imperdiet ex neque sed nisl. Praesent dignissim justo ligula, dignissim auctor massa elementum sed. Suspendisse pulvinar porta eros, eget commodo nulla euismod vitae. Sed vestibulum ipsum eu ligula euismod euismod. Aenean tincidunt metus id consectetur pretium. Nunc pharetra sagittis porttitor.</p>
</div>
<div class="divider" style="top:749px"></div>

<div class="plan" style="left:230px"><div class="from">STARTING AT</div><div class="price">$ 16.99</div><div class="name">RESELLER HOSTING</div><div class="note">Morbi tempus, elit a luctus sodales mauris estrhoncus urna</div></div>
<div class="plan featured" style="left:483px"><div class="from">STARTING AT</div><div class="price">$ 16.99</div><div class="name">RESELLER HOSTING</div><div class="note">Morbi tempus, elit a luctus sodales mauris estrhoncus urna</div></div>
<div class="plan" style="left:736px"><div class="from">STARTING AT</div><div class="price">$ 16.99</div><div class="name">RESELLER HOSTING</div><div class="note">Morbi tempus, elit a luctus sodales mauris estrhoncus urna</div></div>
<svg class="plan-ribbon" style="left:230px" viewBox="0 0 232 20"><polygon points="0,0 232,4 232,20 8,8" fill="#1fbab5"/></svg>
<svg class="plan-ribbon" style="left:483px" viewBox="0 0 232 20"><polygon points="0,0 232,4 232,20 8,8" fill="#1fbab5"/></svg>
<svg class="plan-ribbon" style="left:736px" viewBox="0 0 232 20"><polygon points="0,0 232,4 232,20 8,8" fill="#1fbab5"/></svg>

<!-- features -->
<section class="features">
  <div class="section-intro" style="top:52px">
    <div class="label" style="font-size:22px">Our Excellent</div>
    <div class="big">Features</div>
    <div class="rule"></div>
    <p>Aenean efficitur mauris faucibus ante viverra, vitae malesuada nisl convallis. Fusce rutrum, neque tempor euismod lacinia, eros lorem imperdiet felis, id sollicitudin orci ligula id mauris. Quisque imperdiet at massa nec sagittis. Vestibulum finibus interdum consectetur. Morbi tempus, elit a luctus sodales, mauris est rhoncus urna, quis imperdiet ex neque sed nisl. Praesent dignissim justo ligula, dignissim auctor massa elementum sed. Suspendisse pulvinar porta eros, eget commodo nulla euismod vitae. Sed vestibulum ipsum eu ligula euismod euismod. Aenean tincidunt metus id consectetur pretium. Nunc pharetra sagittis porttitor.</p>
  </div>
  <div class="divider" style="top:152px"></div>

  <div class="feature" style="left:52px;top:205px">
    <svg width="78" height="78" viewBox="0 0 78 78"><g fill="#1fbab5"><circle cx="39" cy="39" r="26"/><g transform="translate(39 39)"><rect x="-6" y="-37" width="12" height="14"/><rect x="-6" y="23" width="12" height="14"/><rect x="-37" y="-6" width="14" height="12"/><rect x="23" y="-6" width="14" height="12"/><rect x="-6" y="-37" width="12" height="14" transform="rotate(45)"/><rect x="-6" y="-37" width="12" height="14" transform="rotate(135)"/><rect x="-6" y="-37" width="12" height="14" transform="rotate(225)"/><rect x="-6" y="-37" width="12" height="14" transform="rotate(315)"/></g></g><circle cx="39" cy="39" r="11" fill="#f5f6f6"/></svg>
    <h3>Loads Of Setting</h3>
    <p>Sed vestibulum ipsum eu ligula euismod euismod. Aenean tincidu metus id consectetur pretium. Nunc pharetra sagittis porttitor. In effici tempor mi, a posuere purus volutpat id. Duis vitae quam nec neque ultrices</p>
  </div>
  <div class="feature" style="left:623px;top:205px">
    <svg width="86" height="60" viewBox="0 0 86 60"><path d="M18 56a16 16 0 0 1-2-32 22 22 0 0 1 42-8 16 16 0 0 1 14 12 14 14 0 0 1-2 28z" fill="#1fbab5"/></svg>
    <h3 style="left:111px">Hosting In The Cloud</h3>
    <p style="left:111px">Cras interdum dui ut euismod dictum. Proin scelerisque mattis tor Nulla ut vulputate leo. Nam vel convallis orci. Aliquam nec mi tellus. rutrum semper lorem, in auctor odio suscipit id.</p>
  </div>
  <div class="feature" style="left:52px;top:322px">
    <svg width="80" height="70" viewBox="0 0 80 70"><circle cx="40" cy="40" r="28" fill="#1fbab5"/><path d="M40 40V12a28 28 0 0 1 28 28z" fill="#8fdcd8"/><rect x="0" y="16" width="34" height="6" fill="#1fbab5"/><rect x="0" y="28" width="26" height="6" fill="#1fbab5"/><rect x="0" y="40" width="30" height="6" fill="#1fbab5"/></svg>
    <h3>Unlimited Disk Space</h3>
    <p>Cras interdum dui ut euismod dictum. Proin scelerisque mattis tor Nulla ut vulputate leo. Nam vel convallis orci. Aliquam nec mi tellus. rutrum semper lorem, in auctor odio suscipit id.</p>
  </div>
  <div class="feature" style="left:623px;top:322px">
    <svg width="86" height="60" viewBox="0 0 86 60"><path d="M8 50a35 35 0 0 1 70 0" fill="none" stroke="#1fbab5" stroke-width="10"/><path d="M43 50 62 28" stroke="#1fbab5" stroke-width="5"/><circle cx="43" cy="50" r="7" fill="#1fbab5"/></svg>
    <h3 style="left:111px">Amazing Perfomance Servers</h3>
    <p style="left:111px">Sed vestibulum ipsum eu ligula euismod euismod. Aenean tincidu metus id consectetur pretium. Nunc pharetra sagittis porttitor. In effici tempor mi, a posuere purus volutpat id. Duis vitae quam nec neque ultrices</p>
  </div>
  <div class="feature" style="left:52px;top:445px">
    <svg width="80" height="70" viewBox="0 0 80 70"><path d="M16 46a14 14 0 0 1-1-28 20 20 0 0 1 38-6 15 15 0 0 1 13 11 12 12 0 0 1-2 23z" fill="#1fbab5"/><rect x="14" y="42" width="52" height="10" rx="3" fill="#1fbab5" stroke="#f5f6f6" stroke-width="2"/><rect x="14" y="54" width="52" height="10" rx="3" fill="#1fbab5" stroke="#f5f6f6" stroke-width="2"/></svg>
    <h3>Business Hosting Solutions</h3>
    <p>Sed vestibulum ipsum eu ligula euismod euismod. Aenean tincidu metus id consectetur pretium. Nunc pharetra sagittis porttitor. In effici tempor mi, a posuere purus volutpat id. Duis vitae quam nec neque ultrices</p>
  </div>
  <div class="feature" style="left:623px;top:445px">
    <svg width="80" height="76" viewBox="0 0 80 76"><path d="M66 22A30 30 0 1 0 70 44" fill="none" stroke="#1fbab5" stroke-width="7"/><polygon points="58,12 74,12 70,28" fill="#1fbab5"/><text x="38" y="48" text-anchor="middle" font-family="Lato,Arial,sans-serif" font-weight="900" font-size="24" fill="#1fbab5">24</text></svg>
    <h3 style="left:111px">24/7 Live Support</h3>
    <p style="left:111px">Cras interdum dui ut euismod dictum. Proin scelerisque mattis tor Nulla ut vulputate leo. Nam vel convallis orci. Aliquam nec mi tellus. rutrum semper lorem, in auctor odio suscipit id.</p>
  </div>
</section>

<!-- blog -->
<section class="blog">
  <div class="section-intro" style="top:50px">
    <div class="label" style="font-size:22px">Latest</div>
    <div class="big">Blog</div>
    <div class="rule"></div>
    <p>Aenean efficitur mauris faucibus ante viverra, vitae malesuada nisl convallis. Fusce rutrum, neque tempor euismod lacinia, eros lorem imperdiet felis, id sollicitudin orci ligula id mauris. Quisque imperdiet at massa nec sagittis. Vestibulum finibus interdum consectetur. Morbi tempus, elit a luctus sodales, mauris est rhoncus urna, quis imperdiet ex neque sed nisl. Praesent dignissim justo ligula, dignissim auctor massa elementum sed. Suspendisse pulvinar porta eros, eget commodo nulla euismod vitae.</p>
  </div>
  <div class="divider" style="top:154px"></div>
</section>

<article class="post" style="left:52px">
  <div class="post-date">17<sup>th</sup><br>Feb</div>
  <h3>Lorem ipsum dolor sit amet, consectetuer adipiscing elit.</h3>
  <div class="byline">Posted by : Mara Quillon <span class="stars">★★★★★</span></div>
  <div class="post-image" role="img" aria-label="Photo of a technician working beside server racks" style="background:linear-gradient(90deg,#7d8a93,#b7c0c6 50%,#4e5860)"></div>
  <p>Lorem ipsum dolor sit amet, consectetuer adipiscing elit, sed diam nonummy nibh euismod tincidunt ut laoreet dolore magna aliquam erat volutpat. Ut wisi enim ad minim veniam,</p>
  <div class="share"><span></span><span></span><span></span><span></span><span></span></div>
</article>
<article class="post" style="left:638px">
  <div class="post-date">17<sup>th</sup><br>Feb</div>
  <h3>Lorem ipsum dolor sit amet, consectetuer adipiscing elit.</h3>
  <div class="byline">Posted by : Mara Quillon <span class="stars">★★★★★</span></div>
  <div class="post-image" role="img" aria-label="Photo of rows of blue-lit data centre servers" style="background:linear-gradient(90deg,#2f5f80,#5fa2c6 50%,#234a66)"></div>
  <p>Lorem ipsum dolor sit amet, consectetuer adipiscing elit, sed diam nonummy nibh euismod tincidunt ut laoreet dolore magna aliquam erat volutpat. Ut wisi enim ad minim veniam,</p>
  <div class="share"><span></span><span></span><span></span><span></span><span></span></div>
</article>

<!-- testimonials -->
<div class="section-intro" style="top:2123px">
  <div class="label" style="font-size:22px">Our Clients</div>
  <div class="big">Says</div>
  <div class="rule"></div>
  <p>Aenean efficitur mauris faucibus ante viverra, vitae malesuada nisl convallis. Fusce rutrum, neque tempor euismod lacinia, eros lorem imperdiet felis, id sollicitudin orci ligula id mauris. Quisque imperdiet at massa nec sagittis. Vestibulum finibus interdum consectetur. Morbi tempus, elit a luctus sodales, mauris est rhoncus urna, quis imperdiet ex neque sed nisl. Praesent dignissim justo ligula, dignissim auctor massa elementum sed. Suspendisse pulvinar porta eros, eget commodo nulla euismod vitae.</p>
</div>
<div class="divider" style="top:2229px"></div>

<div class="quote" style="left:110px;top:2282px;width:392px;text-align:right">
  <strong>Consectetuer Adipiscing</strong>
  <span class="role">Porta - <em>Eros Elit</em></span>
  Lorem ipsum dolor sit amet, consectetuer adipiscing elit, sed diam tincidunt ut laoreet dolore magna aliquam
</div>
<div class="avatar" role="img" aria-label="Client portrait photo" style="left:521px;top:2277px;width:96px;height:96px;background:linear-gradient(#c9b8a8,#6d7780)"></div>
<div class="avatar" role="img" aria-label="Client portrait photo" style="left:579px;top:2373px;width:96px;height:96px;border-color:#2a2f33;background:linear-gradient(#8a6a55,#d9d4cf)"></div>
<div class="quote" style="left:690px;top:2384px;width:420px">
  <strong>Nulla Euismod Vitae</strong>
  <span class="role">Quis - <em>Imperdiet</em></span>
  Lorem ipsum dolor sit amet, consectetuer adipiscing elit, sed diam nonummy nibh euismod tincidunt
</div>

<!-- footer -->
<footer class="site-footer">
  <div class="follow-panel"></div>

  <div class="foot-col" style="left:52px">
    <h4>QUICK LINKS</h4>
    <ul><li>Home</li><li>About</li><li>Domains</li><li>Email</li><li>Hosting</li><li>Dedicated Server</li><li>Faq</li><li>Blog</li><li>Contact Us</li></ul>
  </div>
  <div class="foot-sep" style="left:258px"></div>
  <div class="foot-col" style="left:305px">
    <h4>SERVICES</h4>
    <ul><li>Domain Names</li><li>SiteDesigner</li><li>Web Hosting</li><li>Premium Web Hosting</li><li>Reseller Hosting</li><li>Virtual Private Servers</li><li>Hybrid Servers</li><li>Dedicated Servers</li><li>Email Hosting</li></ul>
  </div>
  <div class="foot-sep" style="left:528px"></div>
  <div class="foot-col" style="left:579px;width:250px">
    <h4 style="width:auto;border-bottom:0">CONTACT DETAILS</h4>
    <div class="contact-row" style="margin-top:8px"><span class="ico"><svg width="10" height="14" viewBox="0 0 10 14"><path d="M5 0a5 5 0 0 1 5 5c0 4-5 9-5 9S0 9 0 5a5 5 0 0 1 5-5z" fill="#fff"/><circle cx="5" cy="5" r="2" fill="#1fbab5"/></svg></span><span><b style="color:#fff">Our Server Lantern</b><br>Diam nonummy nibh,<br>euismo tincidunt ut laoreet ut<br>laoreet dolore magna<br>123456</span></div>
    <div class="contact-row" style="margin-top:18px"><span class="ico"><svg width="12" height="12" viewBox="0 0 12 12"><path d="M2 0h3l1 3-2 1a7 7 0 0 0 4 4l1-2 3 1v3a2 2 0 0 1-2 2A10 10 0 0 1 0 2a2 2 0 0 1 2-2z" fill="#fff"/></svg></span><span style="line-height:22px">123-555-0178</span></div>
    <div class="contact-row" style="margin-top:18px"><span class="ico"><svg width="12" height="9" viewBox="0 0 12 9"><rect width="12" height="9" fill="#fff"/><path d="M0 0l6 5 6-5" fill="none" stroke="#1fbab5" stroke-width="1.2"/></svg></span><span style="line-height:22px">info@ourserverlantern.com</span></div>
  </div>

  <div class="follow" style="position:absolute;left:907px;top:35px">
    <h4>FOLLOW US</h4>
    <div class="socials"><span></span><span></span><span></span><span></span><span></span></div>
    <h4>LEAVE US A MESSAGE</h4>
    <div class="email-field">Email Address</div>
    <span class="submit">SUBMIT</span>
  </div>
</footer>

<div class="bottom-bar">
  <div class="copy">Copyright © 2015 Our Server Lantern | All rights reserved.</div>
  <nav><span>Support</span><span>Privacy</span><span>Terms</span></nav>
</div>

</body>
</html>
```